Flyer for the Harvest Lantern Gathering 2018

Design a flyer for our annual conference with basic information about the conference: conference logo and year,

Location:
Tolvane Community Center (Downtown Portland)
482 Wexmoor Street, Portland, ME 04107,

Date:
August 24th, 25th and 26th, 2018
Start time 6:00PM

I would like the following three words added to the flyer. These words describe the vision of the conference:
Prophetic, Worship, Prayer

```html
<!DOCTYPE html>
<html lang="en">
<head>
<meta charset="utf-8">
<title>Harvest Lantern Gathering 2018</title>
<link href="https://fonts.googleapis.com/css2?family=Open+Sans:wght@600;700&family=Montserrat:wght@400&display=swap" rel="stylesheet">
<style>
  :root {
    --sky-dark: #1f2021;
    --sky-mid: #34373a;
    --sky-glow: #45484b;
    --ring-orange: #e8912b;
    --gold: #f2c862;
    --orange: #f08a2b;
    --white: #f4f4f4;
  }
  html, body {
    margin: 0;
    padding: 0;
    overflow: hidden;
    background: var(--sky-dark);
  }
  .flyer {
    position: relative;
    width: 1200px;
    height: 800px;
    overflow: hidden;
    font-family: "Open Sans", Arial, sans-serif;
    text-align: center;
  }
  .backdrop {
    position: absolute;
    inset: 0;
    background:
      radial-gradient(ellipse 520px 380px at 760px 560px, var(--sky-glow) 0%, rgba(69,72,75,0) 70%),
      linear-gradient(180deg, var(--sky-dark) 0%, var(--sky-mid) 55%, #2a2c2e 100%);
  }
  .brand {
    position: absolute;
    left: 0;
    right: 0;
    top: 70px;
  }
  .brand-ring {
    display: block;
    margin: 0 auto;
  }
  .brand-name {
    margin: 24px 0 0;
    font-family: "Open Sans", Arial, sans-serif;
    font-weight: 600;
    font-size: 54px;
    letter-spacing: 4px;
    line-height: 1;
    color: var(--white);
  }
  .vision {
    position: absolute;
    left: 0;
    right: 0;
    top: 400px;
    margin: 0;
    font-weight: 700;
    font-size: 39px;
    letter-spacing: 2.5px;
    color: var(--gold);
  }
  .schedule {
    position: absolute;
    left: 0;
    right: 0;
    top: 490px;
    margin: 0;
    font-weight: 700;
    font-size: 33px;
    line-height: 44px;
    letter-spacing: 0.5px;
    color: var(--orange);
  }
  .venue {
    position: absolute;
    left: 0;
    right: 0;
    top: 648px;
    margin: 0;
    font-family: "Montserrat", Arial, sans-serif;
    font-weight: 400;
    font-size: 25px;
    line-height: 31px;
    letter-spacing: 2.6px;
    color: var(--white);
    font-style: normal;
  }
</style>
</head>
<body>
<main class="flyer">
  <div class="backdrop" role="img" aria-label="Dusky evening sky photograph with a silhouetted person raising hands in worship"></div>

  <header class="brand">
    <svg class="brand-ring" width="236" height="236" viewBox="0 0 236 236" aria-hidden="true">
      <circle cx="118" cy="118" r="112" fill="none" stroke="var(--ring-orange)" stroke-width="4"/>
    </svg>
    <h1 class="brand-name">HARVESTCON</h1>
  </header>

  <p class="vision">PROPHETIC • WORSHIP • PRAYER</p>

  <p class="schedule">
    AUGUST 24TH, 25TH &amp; 26TH, 2018<br>
    START TIME 6:00PM
  </p>

  <address class="venue">
    TOLVANE COMMUNITY CENTER (DOWNTOWN PORTLAND)<br>
    482 WEXMOOR STREET, PORTLAND, ME 04107,
  </address>
</main>
</body>
</html>
```